Varnock Travel letterhead design

We need a design for a simple document where we can dump our own information within it. A simple letterhead style. No address or phone details etc are required. More just our logo and free format. Hope this makes sense !

```html
<!DOCTYPE html>
<html lang="en">
<head>
<meta charset="utf-8">
<title>Varnock Travel Letterhead Set</title>
<link href="https://fonts.googleapis.com/css2?family=Arimo:wght@400;700&display=swap" rel="stylesheet">
<style>
  :root {
    --navy: #1f4477;
    --silver: #b7b8bd;
    --paper: #ffffff;
    --backdrop: #3a3a3a;
    --ghost: #f1f1f2;
  }
  * { margin: 0; padding: 0; box-sizing: border-box; }
  html, body {
    width: 1200px;
    height: 900px;
    overflow: hidden;
    background: var(--backdrop);
    font-family: "Arimo", Arial, sans-serif;
  }
  .stationery-set {
    position: relative;
    width: 1200px;
    height: 900px;
  }
  .sheet {
    position: absolute;
    top: 215px;
    width: 333px;
    height: 470px;
    background: var(--paper);
    overflow: hidden;
  }
  .sheet--classic { left: 86px; }
  .sheet--pattern { left: 434px; }
  .sheet--sidebar { left: 782px; }

  .brand-name {
    position: absolute;
    top: 24px;
    left: 0;
    width: 100%;
    text-align: center;
    color: var(--navy);
    font-weight: 700;
    font-size: 21px;
    letter-spacing: -0.3px;
    white-space: nowrap;
  }

  .footer-swoop {
    position: absolute;
    left: 0;
    bottom: 0;
    width: 333px;
    height: 52px;
  }

  .ghost-name {
    position: absolute;
    color: var(--ghost);
    font-weight: 700;
    white-space: nowrap;
    letter-spacing: -1px;
  }
  .ghost-name--large { top: 80px; left: -30px; font-size: 80px; }
  .ghost-name--medium { top: 240px; left: 120px; font-size: 46px; }
  .ghost-name--low { top: 360px; left: -130px; font-size: 46px; }
  .ghost-name--small { top: 376px; left: 212px; font-size: 19px; letter-spacing: -0.3px; }

  .side-band {
    position: absolute;
    top: 0;
    left: 0;
    width: 77px;
    height: 100%;
    background: var(--navy);
    display: flex;
    justify-content: center;
    align-items: flex-start;
    padding-top: 18px;
  }
  .side-band-name {
    writing-mode: vertical-rl;
    transform: rotate(180deg);
    color: var(--paper);
    font-weight: 700;
    font-size: 24px;
    letter-spacing: -0.3px;
    white-space: nowrap;
    line-height: 1;
  }
</style>
</head>
<body>
  <main class="stationery-set">

    <section class="sheet sheet--classic">
      <p class="brand-name">Varnock Travel Corporation</p>
      <svg class="footer-swoop" viewBox="0 0 333 52" aria-hidden="true">
        <path d="M120 26 Q250 20 333 0 L333 16 Q260 24 150 27 Z" fill="var(--silver)"/>
        <path d="M0 20 Q160 34 333 18 L333 52 L0 52 Z" fill="var(--navy)"/>
      </svg>
    </section>

    <section class="sheet sheet--pattern">
      <span class="ghost-name ghost-name--large">Varnock Travel</span>
      <span class="ghost-name ghost-name--medium">Varnock Travel</span>
      <span class="ghost-name ghost-name--low">Varnock Travel</span>
      <span class="ghost-name ghost-name--small">Varnock Travel</span>
      <p class="brand-name">Varnock Travel Corporation</p>
      <svg class="footer-swoop" viewBox="0 0 333 52" aria-hidden="true">
        <path d="M120 26 Q250 20 333 0 L333 16 Q260 24 150 27 Z" fill="var(--silver)"/>
        <path d="M0 20 Q160 34 333 18 L333 52 L0 52 Z" fill="var(--navy)"/>
      </svg>
    </section>

    <section class="sheet sheet--sidebar">
      <div class="side-band">
        <p class="side-band-name">Varnock Travel</p>
      </div>
    </section>

  </main>
</body>
</html>
```